Wholesale Fashion Agent

Industry/Entity Type

Fashion

Contact Information for Business Card

I have attached the previous logo, we are wanting to re-vamp with black and white only. Sharp and more modern.

Mirela Stonecroft Agencies back of card
address (to be advised, as we are moving)

MS Agencies front of card, with Fashion Agent on the front

```html
<!DOCTYPE html>
<html lang="en">
<head>
<meta charset="utf-8">
<title>MS Agencies – Business Card</title>
<link rel="stylesheet" href="https://fonts.googleapis.com/css2?family=Questrial&display=swap">
<style>
  :root {
    --backdrop: #cdb49b;
    --card-black: #111111;
    --card-black-soft: #1d1d1d;
    --ink-white: #f4f4f4;
    --ink-grey: #d6d6d6;
    --rule: #cfcfcf;
    --band-light: #ffffff;
    --band-shade: #c9c9c9;
    --ghost: rgba(255, 255, 255, 0.07);
  }
  * { margin: 0; padding: 0; box-sizing: border-box; }
  html, body { width: 1200px; height: 1000px; overflow: hidden; }
  body {
    background: var(--backdrop);
    font-family: "Questrial", "Century Gothic", sans-serif;
    color: var(--ink-white);
    position: relative;
  }
  .card {
    position: absolute;
    left: 250px;
    width: 700px;
    height: 400px;
    overflow: hidden;
    background: radial-gradient(ellipse at 40% 20%, var(--card-black-soft), var(--card-black) 70%);
    box-shadow: 0 14px 30px rgba(0, 0, 0, 0.35);
  }
  .card--front { top: 50px; }
  .card--back { top: 550px; }

  /* front */
  .brand-lockup {
    position: absolute;
    left: 0; right: 0; top: 95px;
    display: flex; flex-direction: column; align-items: center;
  }
  .brand-ring {
    width: 120px; height: 120px; border-radius: 50%;
    border: 4px solid var(--ink-white);
  }
  .brand-name {
    margin-top: 22px;
    padding: 8px 18px 0;
    border-top: 1px solid var(--ink-white);
    font-size: 40px; letter-spacing: 2px; text-transform: uppercase;
  }

  /* back */
  .side-band {
    position: absolute; left: 75px; top: 0; width: 62px; height: 100%;
    background: linear-gradient(90deg, var(--band-shade), var(--band-light) 45%, var(--band-shade));
  }
  .band-disc {
    position: absolute; left: 54px; top: 105px; width: 104px; height: 104px;
    border-radius: 50%; background: var(--card-black);
    border: 4px solid var(--band-light);
    box-shadow: inset 0 0 0 6px var(--card-black), inset 0 0 0 8px var(--ink-white);
  }
  .ghost-ring {
    position: absolute; right: -150px; top: -60px; width: 420px; height: 420px;
    border-radius: 50%; border: 22px solid var(--ghost);
  }
  .agent-name {
    position: absolute; left: 205px; top: 52px;
    font-size: 27px; letter-spacing: 0.5px; text-transform: uppercase;
  }
  .agent-title {
    position: absolute; left: 205px; top: 86px;
    font-size: 21px; color: var(--ink-grey); text-transform: uppercase;
  }
  .contact-list { position: absolute; left: 200px; top: 128px; width: 470px; list-style: none; }
  .contact-item {
    display: flex; align-items: flex-end; height: 44px;
    border-bottom: 1px solid var(--rule);
    padding-bottom: 6px;
  }
  .contact-item:last-child { border-bottom: none; height: 76px; }
  .contact-icon {
    flex: none; width: 26px; height: 26px; margin-right: 16px;
    border-radius: 50%; background: var(--ink-white);
    display: flex; align-items: center; justify-content: center;
  }
  .contact-icon svg { width: 16px; height: 16px; }
  .contact-text { font-size: 19px; line-height: 1.3; letter-spacing: 0.3px; }
</style>
</head>
<body>
  <section class="card card--front" aria-label="Card front">
    <div class="brand-lockup">
      <div class="brand-ring"></div>
      <div class="brand-name">MS Agencies</div>
    </div>
  </section>

  <section class="card card--back" aria-label="Card back">
    <div class="ghost-ring"></div>
    <div class="side-band"></div>
    <div class="band-disc"></div>

    <h1 class="agent-name">Mirela Stonecroft</h1>
    <p class="agent-title">Fashion Agent</p>

    <ul class="contact-list">
      <li class="contact-item">
        <span class="contact-icon"><svg viewBox="0 0 16 16"><path d="M4 2l2.5 3-1.5 1.5a8 8 0 0 0 4.5 4.5L11 9.5l3 2.5-1.5 2.5C7 14 2 9 1.5 3.5z" fill="#111"/></svg></span>
        <span class="contact-text">07-35550182</span>
      </li>
      <li class="contact-item">
        <span class="contact-icon"><svg viewBox="0 0 16 16"><rect x="4.5" y="1.5" width="7" height="13" rx="1.2" fill="none" stroke="#111" stroke-width="1.5"/><rect x="6" y="3.5" width="4" height="5" fill="#111"/></svg></span>
        <span class="contact-text">0491 570 236</span>
      </li>
      <li class="contact-item">
        <span class="contact-icon"><svg viewBox="0 0 16 16" fill="none" stroke="#111" stroke-width="1.2"><circle cx="8" cy="8" r="6.5"/><ellipse cx="8" cy="8" rx="3" ry="6.5"/><path d="M1.5 8h13M2.5 5h11M2.5 11h11"/></svg></span>
        <span class="contact-text">www.msagencies.com.au</span>
      </li>
      <li class="contact-item">
        <span class="contact-icon"><svg viewBox="0 0 16 16" fill="none" stroke="#111" stroke-width="1.4"><rect x="1.5" y="3.5" width="13" height="9"/><path d="M1.5 3.5L8 9l6.5-5.5"/></svg></span>
        <span class="contact-text">mirela@msagencies.com.au</span>
      </li>
      <li class="contact-item">
        <span class="contact-icon"><svg viewBox="0 0 16 16"><path d="M8 1a5 5 0 0 1 5 5c0 4-5 9-5 9S3 10 3 6a5 5 0 0 1 5-5z" fill="#111"/><circle cx="8" cy="6" r="1.8" fill="#f4f4f4"/></svg></span>
        <span class="contact-text">Unit 7, 42 Harwell Lane<br>ASHGROVE QLD 4060</span>
      </li>
    </ul>
  </section>
</body>
</html>
```